General Graphic Chart and several template items to create

We need the following to be created for our company where we already have a logo set which we are not changing, but we are lacking all additional items that have a set graphic chart and templates to play with. The winner of this contest will be receiving requests on ongoing basis for graphic by us and some co-branded with our clients.

We need to have created the following in a templated setup where our staff can use the graphical layout and edit the content by themselves. The inspiration is the current logo of the company, but the whole needs to inspire "technology", "visual", "dynamic", "serious", "not to yellowish like in the logo":
1. Stationary
2. Website Banners (advertisement banners)
3. Offers sent out to B2B customers
4. General 1 pagers leaflets to put inside brochures
5. PPT presentation template
6. Tri-fold brochure
7. A mascot

This might sound a lot but it is an exercise over time for the winner with good reward.

Thanks

```html
<!DOCTYPE html>
<html lang="en">
<head>
<meta charset="utf-8">
<title>Part 01 – Sample Web Banners</title>
<link href="https://fonts.googleapis.com/css2?family=Montserrat:wght@700;800&family=Raleway:wght@300;400;500&display=swap" rel="stylesheet">
<style>
  :root{
    --sheet:#aeabab;
    --teal:#13384a;
    --teal-deep:#0d2633;
    --grey:#6d6e71;
    --orange:#f5a81c;
    --purple:#8a47c8;
    --violet:#6f5cc4;
    --magenta:#b22fa6;
    --navy:#1c1f5e;
    --paper:#ffffff;
    --paper-cool:#f3f6fa;
  }
  html,body{margin:0;padding:0;}
  body{width:734px;height:1200px;overflow:hidden;background:var(--sheet);position:relative;font-family:"Raleway",sans-serif;}
  .sheet-title{position:absolute;top:36px;left:0;width:734px;text-align:center;margin:0;font-family:"Raleway",sans-serif;font-weight:400;font-size:30px;color:var(--paper);letter-spacing:.5px;}
  .banner{position:absolute;width:570px;height:194px;box-shadow:4px 8px 12px rgba(0,0,0,.35);overflow:hidden;background:var(--paper);}
  .banner svg{display:block;width:100%;height:100%;}
  .banner-1{left:80px;top:124px;}
  .banner-2{left:80px;top:387px;}
  .banner-3{left:83px;top:657px;height:189px;}
  .banner-4{left:82px;top:920px;height:193px;}
  .sample-label{position:absolute;left:682px;width:0;height:0;}
  .sample-label span{position:absolute;transform:translate(-50%,-50%) rotate(-90deg);white-space:nowrap;font-family:"Raleway",sans-serif;font-size:24px;font-weight:400;color:var(--paper);}
  .display{font-family:"Montserrat",sans-serif;font-weight:800;}
  .brand{font-family:"Montserrat",sans-serif;font-weight:700;}
  .light{font-family:"Raleway",sans-serif;font-weight:300;}
  .body-copy{font-family:"Raleway",sans-serif;font-weight:400;}
</style>
</head>
<body>

<h1 class="sheet-title">Part 01 - Sample Web Banners</h1>

<!-- Banner 1 -->
<div class="banner banner-1">
  <svg viewBox="0 0 1171 397" preserveAspectRatio="none">
    <defs>
      <linearGradient id="city-a" x1="0" y1="0" x2="1" y2="1">
        <stop offset="0" stop-color="#1a2733"/>
        <stop offset=".45" stop-color="#6b7f90"/>
        <stop offset=".75" stop-color="#dfe6ec"/>
        <stop offset="1" stop-color="#55697a"/>
      </linearGradient>
      <radialGradient id="disc" cx=".45" cy=".4" r=".6">
        <stop offset=".6" stop-color="#ffffff"/>
        <stop offset="1" stop-color="#d5d6d8"/>
      </radialGradient>
    </defs>
    <rect width="1171" height="397" fill="url(#city-a)" role="img" aria-label="Photo of glass skyscrapers seen from street level"/>
    <path d="M0,310 C260,390 520,360 760,280 L1171,230 L1171,397 L0,397 Z" fill="var(--teal)" opacity=".92"/>
    <path d="M0,318 C260,400 520,370 780,270" fill="none" stroke="var(--grey)" stroke-width="34"/>
    <rect x="35" y="33" width="556" height="216" fill="var(--teal)" opacity=".9"/>
    <text x="66" y="108" class="display" font-size="56" fill="var(--paper)">BANNER</text>
    <text x="66" y="155" class="display" font-size="30" fill="var(--paper)">TEXT HERE</text>
    <text x="66" y="186" class="light" font-size="16.5" fill="var(--paper)">Lorem ipsum dolor sit amet, consectetuer adipiscing elit, sed</text>
    <text x="66" y="211" class="light" font-size="16.5" fill="var(--paper)">diam nonummy nibh euismod tincidunt.</text>
    <circle cx="690" cy="395" r="128" fill="var(--grey)"/>
    <circle cx="690" cy="395" r="112" fill="url(#disc)"/>
    <circle cx="1048" cy="255" r="80" fill="var(--grey)"/>
    <circle cx="1048" cy="255" r="64" fill="url(#disc)"/>
    <circle cx="1060" cy="110" r="105" fill="var(--grey)"/>
    <circle cx="1060" cy="110" r="90" fill="url(#disc)"/>
    <circle cx="835" cy="200" r="190" fill="var(--grey)"/>
    <circle cx="835" cy="200" r="166" fill="url(#disc)"/>
    <circle cx="708" cy="197" r="17" fill="var(--orange)"/>
    <text x="736" y="216" class="brand" font-size="50" textLength="225" lengthAdjust="spacingAndGlyphs" fill="var(--teal)">nexalink</text>
    <text x="1158" y="380" text-anchor="end" class="body-copy" font-size="16" letter-spacing="3.5" fill="var(--paper)">WWW.NEXALINK.COM</text>
  </svg>
</div>
<div class="sample-label" style="top:221px"><span>Sample 01</span></div>

<!-- Banner 2 -->
<div class="banner banner-2">
  <svg viewBox="0 0 1171 397" preserveAspectRatio="none">
    <defs>
      <linearGradient id="city-b" x1="0" y1="0" x2="1" y2="1">
        <stop offset="0" stop-color="#0f3143"/>
        <stop offset=".6" stop-color="#173e51"/>
        <stop offset="1" stop-color="#0b1e29"/>
      </linearGradient>
      <linearGradient id="stripe-violet" x1="0" y1="0" x2="1" y2="1">
        <stop offset="0" stop-color="var(--violet)"/>
        <stop offset="1" stop-color="#c04fd6"/>
      </linearGradient>
      <linearGradient id="stripe-magenta" x1="0" y1="0" x2="1" y2="1">
        <stop offset="0" stop-color="#6a2aa8"/>
        <stop offset="1" stop-color="var(--magenta)"/>
      </linearGradient>
    </defs>
    <rect width="1171" height="397" fill="var(--paper)"/>
    <polygon points="560,0 1171,0 1171,397 720,397 430,80" fill="url(#city-b)" role="img" aria-label="Photo of dark office towers seen from below"/>
    <polygon points="300,0 345,0 345,50" fill="var(--violet)"/>
    <polygon points="365,0 400,0 600,230 595,320 365,70" fill="url(#stripe-violet)" opacity=".9"/>
    <polygon points="420,0 470,0 790,260 660,260" fill="url(#stripe-magenta)" opacity=".9"/>
    <polygon points="475,0 580,0 670,90 670,155" fill="var(--magenta)" opacity=".9"/>
    <polygon points="530,0 605,0 670,65 670,150" fill="var(--orange)"/>
    <polygon points="605,0 660,0 770,120 790,200" fill="var(--magenta)" opacity=".85"/>
    <polygon points="625,250 680,250 740,370 650,330" fill="url(#stripe-violet)"/>
    <polygon points="680,300 710,300 800,397 770,397" fill="var(--purple)"/>
    <polygon points="50,220 200,397 130,397 50,310" fill="url(#stripe-violet)" opacity=".8"/>
    <polygon points="0,290 100,397 35,397 0,360" fill="var(--orange)"/>
    <polygon points="0,310 80,397 60,397 0,335" fill="#d2501f"/>
    <polygon points="0,350 50,397 0,397" fill="var(--magenta)" opacity=".8"/>
    <circle cx="44" cy="97" r="19" fill="var(--orange)"/>
    <text x="76" y="118" class="brand" font-size="56" textLength="234" lengthAdjust="spacingAndGlyphs" fill="var(--teal)">nexalink</text>
    <text x="40" y="197" class="light" font-size="36" fill="#333">TEXT HERE</text>
    <text x="40" y="261" class="light" font-size="18" fill="#555">Lorem ipsum dolor sit amet, consectetur</text>
    <text x="40" y="289" class="light" font-size="18" fill="#555">adipiscing elit. Suspendisse in</text>
    <text x="1007" y="230" text-anchor="middle" class="display" font-size="60" fill="var(--paper)">BANNER</text>
    <text x="1007" y="280" text-anchor="middle" class="body-copy" font-size="20" fill="var(--orange)">YOUR TEXT HERE</text>
  </svg>
</div>
<div class="sample-label" style="top:484px"><span>Sample 02</span></div>

<!-- Banner 3 -->
<div class="banner banner-3">
  <svg viewBox="0 0 1171 387" preserveAspectRatio="none">
    <defs>
      <linearGradient id="city-c" x1="0" y1="0" x2="1" y2="1">
        <stop offset="0" stop-color="#1d1b26"/>
        <stop offset=".55" stop-color="#3b3a44"/>
        <stop offset=".8" stop-color="#a89a86"/>
        <stop offset="1" stop-color="#c9b799"/>
      </linearGradient>
      <linearGradient id="tag" x1="0" y1="0" x2="1" y2="0">
        <stop offset="0" stop-color="#151a45"/>
        <stop offset="1" stop-color="#2a2b7a"/>
      </linearGradient>
    </defs>
    <rect width="1171" height="387" fill="var(--paper-cool)"/>
    <polygon points="0,0 490,0 330,60 590,387 0,387" fill="url(#city-c)" role="img" aria-label="Photo of a skyscraper facade catching the sun"/>
    <polygon points="0,0 490,0 330,180 0,387" fill="#14141c" opacity=".55"/>
    <polygon points="290,0 985,0 1022,52 330,52" fill="var(--teal)"/>
    <polygon points="330,52 410,52 150,387 60,387" fill="var(--teal-deep)" opacity=".6"/>
    <polygon points="0,195 150,387 0,387" fill="var(--orange)"/>
    <polygon points="0,270 90,387 0,387" fill="var(--orange)"/>
    <polygon points="550,335 1022,335 985,387 590,387" fill="var(--teal)"/>
    <text x="42" y="80" class="display" font-size="38" fill="var(--orange)">BANNER</text>
    <text x="57" y="119" class="body-copy" font-size="18" fill="var(--orange)">YOUR TEXT HERE</text>
    <g class="social-links" fill="var(--paper)" font-size="11" font-family="Raleway, sans-serif">
      <circle cx="678" cy="30" r="11" fill="none" stroke="var(--orange)" stroke-width="1.5"/>
      <text x="697" y="34">Chatter</text>
      <circle cx="770" cy="30" r="11" fill="none" stroke="var(--orange)" stroke-width="1.5"/>
      <text x="788" y="34">Snapline</text>
      <circle cx="864" cy="30" r="11" fill="none" stroke="var(--orange)" stroke-width="1.5"/>
      <text x="882" y="34">Chirpnet</text>
    </g>
    <circle cx="880" cy="106" r="19" fill="var(--orange)"/>
    <text x="912" y="126" class="brand" font-size="54" textLength="240" lengthAdjust="spacingAndGlyphs" fill="var(--teal)">nexalink</text>
    <polygon points="532,162 831,162 870,220 571,220" fill="url(#tag)"/>
    <text x="708" y="203" text-anchor="middle" class="light" font-size="32" fill="var(--paper)">TEXT HERE</text>
    <text x="566" y="256" class="light" font-size="17" fill="#444">Lorem ipsum dolor sit amet, consectetuer adipiscing elit, sed</text>
    <text x="566" y="280" class="light" font-size="17" fill="#444">diam nonummy nibh euismod tincidunt.</text>
    <text x="785" y="370" text-anchor="middle" class="body-copy" font-size="17" letter-spacing="4" fill="var(--paper)">WWW.NEXALINK.COM</text>
  </svg>
</div>
<div class="sample-label" style="top:751px"><span>Sample 03</span></div>

<!-- Banner 4 -->
<div class="banner banner-4">
  <svg viewBox="0 0 1168 396" preserveAspectRatio="none">
    <defs>
      <radialGradient id="city-d" cx=".35" cy=".35" r=".7">
        <stop offset="0" stop-color="#f2f2f2"/>
        <stop offset=".55" stop-color="#9a9aa0"/>
        <stop offset="1" stop-color="#2a2a36"/>
      </radialGradient>
      <radialGradient id="city-e" cx=".3" cy=".25" r=".8">
        <stop offset="0" stop-color="#f0f0f0"/>
        <stop offset=".5" stop-color="#8c8a8c"/>
        <stop offset=".85" stop-color="#2b2a3a"/>
        <stop offset="1" stop-color="#c79a4e"/>
      </radialGradient>
    </defs>
    <rect width="1168" height="396" fill="var(--paper)"/>
    <path d="M420,150 C600,60 760,20 680,0 L1168,0 L1168,240 C1000,60 760,90 520,230 Z" fill="var(--teal)"/>
    <path d="M500,225 C760,80 1000,90 1168,250 L1168,210 C1000,40 740,50 470,200 Z" fill="var(--grey)"/>
    <path d="M0,230 C120,320 300,290 500,200 L520,230 C330,350 200,380 0,396 Z" fill="var(--teal)"/>
    <path d="M0,396 L230,396 C300,380 420,330 520,232 L540,260 C430,350 320,396 300,396 Z" fill="var(--grey)"/>
    <circle cx="107" cy="151" r="140" fill="var(--grey)"/>
    <circle cx="107" cy="151" r="128" fill="var(--paper)"/>
    <circle cx="107" cy="151" r="120" fill="url(#city-d)" role="img" aria-label="Photo of a tower facade looking up"/>
    <circle cx="347" cy="211" r="180" fill="var(--grey)"/>
    <circle cx="347" cy="211" r="166" fill="var(--paper)"/>
    <circle cx="347" cy="211" r="156" fill="url(#city-e)" role="img" aria-label="Photo of a stepped skyscraper against a pale sky"/>
    <text x="1155" y="30" text-anchor="end" class="body-copy" font-size="16" letter-spacing="3.5" fill="var(--teal)">WWW.NEXALINK.COM</text>
    <text x="1094" y="268" text-anchor="end" class="light" font-size="34" fill="#333">TEXT HERE</text>
    <circle cx="886" cy="330" r="19" fill="var(--orange)"/>
    <text x="918" y="350" class="brand" font-size="54" textLength="222" lengthAdjust="spacingAndGlyphs" fill="var(--teal)">nexalink</text>
  </svg>
</div>
<div class="sample-label" style="top:1016px"><span>Sample 04</span></div>

</body>
</html>
```